KTJ Business Card

Create a Simple but Elegant business card for a Luxury Off Road Vehicle and Accessories sales Company. Center of Letters we usually fill with red or a carbon fiber we don't want to limit creativity so anything goes. I think we would prefer large logo on the front and a smaller logo with infused QR reader on the back.
Some Ideas to get you heading more in the right direction are to put them on a thicker cardstock with red edges and we would need our logo letter (KTJ) filled in with red. Example is the Vescarelli card in our brief. For the side with our info on it we are looking for our logo to include an embedded QR reader also in our brief.
Information to include 2 bullet points: Luxury Off Road Vehicle Sales / Custom Off Road Bumpers
Address:418 Pellmont Road, Suite 519, The Woodlands, Texas
Phone# 555-314-9027,
Website: WWW.KTJ-TRAILGEAR.EXAMPLE
Facebook: facebook.com/KTJTrailGear
Instagram: instagram.com/ktj_trailgear
Target Market(s)
Exotic Vehicle and Outdoor enthusiasts.
Industry/Entity Type
Business
Look and feel
Each slider illustrates characteristics of the customer's brand and the style your logo design should communicate.

```html
<!DOCTYPE html>
<html lang="en">
<head>
<meta charset="utf-8">
<title>KTJ Business Card</title>
<link rel="stylesheet" href="https://fonts.googleapis.com/css2?family=Open+Sans:ital,wght@0,400;0,600;0,700;0,800;1,400&family=Michroma&display=swap">
<style>
  :root {
    --backdrop: #5b5b5b;
    --card-light: #ffffff;
    --card-dark: #2b2828;
    --ink: #1d1d1d;
    --ink-soft: #2e2e2e;
    --muted: #9a9a9a;
    --on-dark: #ffffff;
    --accent: #c4161c;
  }
  * { margin: 0; padding: 0; box-sizing: border-box; }
  html, body {
    width: 1200px; height: 574px; overflow: hidden;
    background: var(--backdrop);
    font-family: "Open Sans", Arial, sans-serif;
  }
  .canvas { position: relative; width: 1200px; height: 574px; }
  .card { position: absolute; top: 139px; width: 510px; height: 284px; }
  .card--front { left: 81px; background: var(--card-light); color: var(--ink); }
  .card--back { left: 622px; background: var(--card-dark); color: var(--on-dark); }

  .brand { position: absolute; left: 42px; top: 58px; }
  .brand__row { display: flex; align-items: center; gap: 8px; }
  .brand__name {
    font-weight: 800; font-size: 48px; line-height: 1; color: var(--accent);
    letter-spacing: 2px;
  }
  .brand__dot {
    width: 50px; height: 50px; border-radius: 50%;
    border: 6px solid var(--ink);
  }
  .tagline {
    font-family: "Michroma", Arial, sans-serif;
    font-size: 9px; letter-spacing: 0.6px; color: var(--ink);
    margin-top: 5px; white-space: nowrap;
  }

  .person { position: absolute; left: 323px; top: 70px; }
  .person__name { font-size: 20px; font-weight: 600; color: var(--ink); line-height: 1.2; }
  .person__title { font-size: 15px; font-weight: 600; color: var(--muted); margin-top: 4px; margin-left: 3px; }

  .address {
    position: absolute; left: 40px; top: 198px;
    font-size: 13px; line-height: 20.5px; color: var(--ink-soft); font-style: normal;
  }
  .address__web { font-style: italic; letter-spacing: 1.2px; white-space: nowrap; }

  .contact {
    position: absolute; left: 323px; top: 198px;
    font-size: 12.5px; line-height: 20.5px; color: var(--ink-soft);
    list-style: none; white-space: nowrap;
  }
  .contact__label { font-weight: 700; }

  .emblem {
    position: absolute; left: 197px; top: 82px;
    width: 118px; height: 118px; border-radius: 50%;
    background: var(--on-dark);
    display: flex; align-items: center; justify-content: center;
  }
  .emblem__name { font-weight: 800; font-size: 38px; color: var(--accent); letter-spacing: 2px; }
  .services {
    position: absolute; left: 0; right: 0; top: 214px;
    list-style: none; text-align: center;
    font-family: "Michroma", Arial, sans-serif;
    font-size: 9.5px; line-height: 17px; letter-spacing: 1.2px; color: var(--on-dark);
  }
</style>
</head>
<body>
<main class="canvas">
  <section class="card card--front">
    <div class="brand">
      <div class="brand__row">
        <span class="brand__name">KTJ</span>
        <span class="brand__dot"></span>
      </div>
      <p class="tagline">Custom Off-Road Products</p>
    </div>
    <div class="person">
      <p class="person__name">Your name</p>
      <p class="person__title">Job Title</p>
    </div>
    <address class="address">
      <p>418 Pellmont Road, Suite 519</p>
      <p>The Woodlands, Texas</p>
      <p class="address__web">WWW.KTJ-TRAILGEAR.EXAMPLE</p>
    </address>
    <ul class="contact">
      <li><span class="contact__label">P :</span> 555-314-9027</li>
      <li><span class="contact__label">F :</span> facebook.com/KTJTrailGear</li>
      <li><span class="contact__label">I :</span> instagram.com/ktj_trailgear</li>
    </ul>
  </section>

  <section class="card card--back">
    <div class="emblem"><span class="emblem__name">KTJ</span></div>
    <ul class="services">
      <li>Luxury Off Road Vehicle Sales</li>
      <li>Custom Off Road Bumpers</li>
    </ul>
  </section>
</main>
</body>
</html>
```